Starter & Alternator business needs a website

update: very good designs submitted so far. also need this to display well on mobile devices. not sure if wordpress or html/css is better for my needs.

Our existing website is vexlandrib.com and is need of total revamp. Need full design of a website for my business.

We sell and rebuild starters and alternators. Customers bring in the units and we rebuild them. Or we sell them brand new or rebuilt units we have in stock. We do not install units into vehicles like a mechanic would. We strictly rebuild starters and alternators in our shop, sell brand new units over the counter, and we do deliver occasionally as well. We do offer a line of Morlin batteries as well but that is only a small feature of the business.

I would like this website designed and coded. I can upload the files to my web host after completion. I can also add in and modify content like our background info, etc.

I have included an illustrator file that shows some of our signage and logo, etc. I have also included a radio commercial sample so you can get a little better feel for the business. A similar ad does run on the radio currently, slightly different and without the added sound effects.

Update: I do like using photos of real items(starters or alternators etc) for an icon, like a real alternator stock image for the alternator section icon, etc. Maybe incorporate our logo in that design as well. That looks nice as well and may aid in navigation.

For any other design elements, do what you think looks good. Our colors are red/white/blue as seen in the illustrator file. our building is painted with talbot greaves colors, emberglow red and deep harbor for blue.

Here are some examples of rebuilders websites in other markets for reference:

https://brommelgarage.com/starter-alternator-rebuilding/

https://www.quintonmotorworks.com/auto-repairs/alternator-starter-rebuilds.aspx

https://www.lorvexcharging.com/

https://www.damblingwx.com/

The website can have areas for: services and products offered, high output alternators, Morlin Batteries, troubleshooting tips, current specials, contact info and directions/map, etc. Whatever else you feel applies.

At some point I do want to be able to sell items directly online or at least have a secure section for customers to submit invoice payments, but that's not necessarily in scope for this project just something to keep in mind.

Target Market(s)

Mechanics and Managers in fleet shops, construction and marine industries, shipping trades. Also automobile owners who work on their own vehicles. We sell and rebuild starters and alternators for automobiles, heavy duty equipment, forklifts, gradalls, man movers, bobcats, loaders, large tractors and trucks, just about any engine, golf carts, generators, etc.

Industry/Entity Type

Automotive Part

Coding

Coded - Design and coding required

Number of Pages Required

5+ page

Font styles to use
Serif
Sans Serif

Colors
0255a3
ec1f27
ffffff

Requirements
Must have
• Should also display nicely on mobile phones. Highlight our specialty, "Starters & Alternators"

```html
<!DOCTYPE html>
<html lang="en">
<head>
<meta charset="utf-8">
<title>Vexland Rebuilders – Starters &amp; Alternators</title>
<link rel="stylesheet" href="https://fonts.googleapis.com/css2?family=Poppins:wght@300;400;500;600;700;800&display=swap">
<style>
:root{
  --red:#b3262c;
  --red-bright:#e3232b;
  --navy:#1c2c4f;
  --navy-deep:#0d1636;
  --ink:#222;
  --grey:#666;
  --line:#d5d5d5;
  --white:#fff;
  --footer:#111;
}
*{margin:0;padding:0;box-sizing:border-box}
html,body{width:1200px;height:3113px;overflow:hidden}
body{position:relative;font-family:"Poppins",sans-serif;color:var(--ink);background:var(--white)}
.abs{position:absolute}
a{color:inherit;text-decoration:none}

/* hero */
.hero{left:0;top:0;width:1200px;height:539px;background:radial-gradient(ellipse at 30% 40%,#2c2c2c,#111 75%)}
.hero-photo{left:640px;top:40px;width:560px;height:420px;background:radial-gradient(ellipse at 60% 45%,#4a4a4a,#1b1b1b 70%);border-radius:4px}
.hero-photo::after{content:"";position:absolute;right:40px;bottom:40px;width:200px;height:150px;background:linear-gradient(135deg,#d89a20,#8a5a12);opacity:.75;border-radius:4px}
.hero-bracket{left:112px;top:94px}
.hero-title{left:221px;top:185px;color:var(--white);font-size:31px;font-weight:500;line-height:47px}
.hero-title .spec{display:block;color:var(--red);font-size:39px;font-weight:800;line-height:46px}
.hero-tags{left:224px;top:332px;color:var(--white);font-size:30px;font-weight:800;display:flex;align-items:center;gap:10px}
.hero-dots{left:583px;top:466px;display:flex;gap:3px}
.hero-dots span{width:10px;height:10px;border:1px solid var(--red)}
.hero-dots span.on{background:var(--red)}

.brand-tab{left:0;top:463px}
.brand{left:26px;top:492px;display:flex;align-items:center;gap:10px;color:var(--navy);font-weight:700;font-size:19px;letter-spacing:.5px}
.brand i{width:32px;height:32px;border-radius:50%;border:3px solid var(--navy)}

.nav{left:0;top:539px;width:1200px;height:41px;border-bottom:1px solid var(--line)}
.nav a{position:absolute;top:15px;font-size:11px;font-weight:600;color:var(--navy);transform:translateX(-50%);white-space:nowrap}
.nav a.active{color:var(--red)}

/* we do */
.dots-field{left:387px;top:580px;width:593px;height:195px;background:radial-gradient(ellipse at 70% 50%,#e6e6e6,rgba(255,255,255,0) 70%)}
.h2{font-size:36px;font-weight:500;color:var(--ink);display:flex;align-items:center;gap:10px}
.h2 em{font-style:normal;color:var(--red)}
.h2::after{content:"";width:32px;height:2px;background:var(--navy)}
.wedo-title{left:221px;top:696px;font-size:34px}
.wedo-text{left:221px;top:756px;width:399px;font-size:13.5px;line-height:19.6px;color:#333;text-align:justify}
.btn{left:221px;top:894px;display:flex;height:27px;font-size:11px;color:var(--white)}
.btn span{background:var(--red);width:91px;display:flex;align-items:center;justify-content:center}
.btn b{background:var(--navy);width:30px;display:flex;align-items:center;justify-content:center}
.photo-big{left:671px;top:707px;width:224px;height:224px;border-radius:50%;background:radial-gradient(circle at 40% 40%,#b8333a,#6e1418)}
.photo-small{left:834px;top:804px;width:142px;height:142px;border-radius:50%;border:4px solid var(--white);background:radial-gradient(circle at 50% 45%,#8a8a8a,#2e2e2e)}

/* services */
.svc-band{left:0;top:1054px}
.svc-title{left:221px;top:1160px}
.svc-sub{left:221px;top:1208px;font-size:14px;color:#333}
.svc-img{width:244px;height:185px;top:1265px}
.svc-card{top:1424px;width:209px;height:118px;display:flex;align-items:flex-end;justify-content:center;padding-bottom:24px;text-align:center;font-size:13px;font-weight:700;line-height:18px;box-shadow:0 3px 10px rgba(0,0,0,.08)}
.svc-card.light{background:var(--white);color:var(--ink)}
.svc-card.dark{background:var(--red);color:var(--white)}
.svc-icon{position:absolute;top:-31px;left:73px;width:62px;height:62px;border-radius:50%;display:flex;align-items:center;justify-content:center}
.light .svc-icon{background:var(--red)}
.dark .svc-icon{background:var(--white)}

/* blog */
.blog-title{left:221px;top:1752px}
.blog-sub{left:221px;top:1800px;font-size:14px;color:#333}
.post{top:1854px;width:244px}
.post-img{height:126px;background:linear-gradient(135deg,#2a48c4 0 35%,#555 60%,#2b2b2b)}
.post-date{margin-top:14px;font-size:12.5px;color:#333}
.post-meta{margin-top:8px;display:flex;gap:14px;font-size:10.5px;color:#555;align-items:center}
.post-meta span{display:flex;align-items:center;gap:5px}
.post-meta i{width:8px;height:8px;background:var(--red);border-radius:50%}
.post h3{margin-top:6px;font-size:15px;font-weight:400}
.post p{margin-top:4px;font-size:11px;line-height:19px;color:var(--grey)}
.more{display:block;margin-top:6px;font-size:11.5px;font-weight:700;color:var(--red)}
.side{left:780px;top:1854px;width:200px}
.side-item{border-top:1px solid var(--line);width:106px;height:82px}
.side-item h4{font-size:15px;font-weight:400;margin-top:20px;width:200px}
.side-item p{font-size:12.5px;margin-top:3px;width:210px}
.side .more{margin-top:20px}

/* contact band */
.contact{left:0;top:2230px;width:1200px;height:211px;background:linear-gradient(180deg,var(--navy-deep),#16234a)}
.contact-col{top:2270px;width:300px;text-align:center;color:var(--white);font-size:13px;line-height:19px}
.contact-col h5{color:var(--red-bright);font-size:16px;font-weight:400;margin:10px 0 8px}
.contact-col a{display:block;margin-top:4px;color:var(--red-bright);text-decoration:underline;font-size:12.5px}
.divider{top:2257px;width:1px;height:154px;background:rgba(255,255,255,.35)}

.map{left:0;top:2441px;width:1200px;height:316px;background:linear-gradient(120deg,#e7e7e7,#dedede 60%,#d7e5d1)}

/* footer */
.footer{left:0;top:2757px;width:1200px;height:356px;background:radial-gradient(ellipse at 40% 40%,#262626,var(--footer) 70%)}
.foot-brand{left:181px;top:2812px;display:flex;align-items:center;gap:12px;color:var(--white);font-size:26px;font-weight:700;line-height:28px}
.foot-brand i{width:46px;height:46px;border-radius:50%;border:3px solid var(--white)}
.foot-about{left:181px;top:2889px;width:262px;color:var(--white);font-size:10.5px;line-height:15.4px;text-align:justify}
.foot-col{top:2812px;color:var(--white)}
.foot-col h6{color:var(--red-bright);font-size:14.5px;font-weight:600}
.foot-col h6::after{content:"";display:block;width:30px;height:2px;background:var(--white);margin-top:8px}
.foot-col ul{list-style:none;margin-top:10px}
.foot-col li{font-size:10.5px;height:24px;display:flex;align-items:center;gap:10px}
.foot-col li::before{content:"»";color:var(--red-bright);font-size:13px}
.news-text{font-size:10.5px;line-height:16px;margin-top:12px;width:175px}
.news-form{margin-top:16px;display:flex;width:167px;height:25px}
.news-form span{flex:1;background:var(--white);border-radius:13px 0 0 13px;font-size:7px;color:#999;display:flex;align-items:center;padding-left:14px}
.news-form b{width:34px;background:var(--red-bright);border-radius:0 13px 13px 0;font-size:9px;display:flex;align-items:center;justify-content:center}
.follow{margin-top:12px;font-size:10px;font-weight:700;display:flex;align-items:center;gap:6px}
.follow i{width:13px;height:13px;border-radius:50%;background:#3b6bd6}
.foot-line{left:0;top:3065px;width:1200px;height:1px;background:rgba(255,255,255,.2)}
.copy{left:0;top:3080px;width:1200px;text-align:center;color:var(--white);font-size:10px}
</style>
</head>
<body>

<!-- hero -->
<div class="abs hero"></div>
<div class="abs hero-photo" role="img" aria-label="Photo of alternators, a starter and a stack of Morlin batteries"></div>
<svg class="abs hero-bracket" width="188" height="290" viewBox="0 0 188 290">
  <path d="M1 1H186V51H52V288H1Z" fill="#14213f" stroke="#fff" stroke-width="2"/>
</svg>
<div class="abs hero-title">Vexland<br>Rebuilders Kailoa<span class="spec">Starters &amp; Alternators</span></div>
<div class="abs hero-tags">Automotive
  <svg width="16" height="34" viewBox="0 0 16 34"><path d="M10 0 2 18h6L4 34 15 13H9Z" fill="#b3262c"/></svg>Marine
  <svg width="16" height="34" viewBox="0 0 16 34"><path d="M10 0 2 18h6L4 34 15 13H9Z" fill="#b3262c"/></svg>Heavy Duty</div>
<div class="abs hero-dots"><span></span><span class="on"></span><span></span></div>

<svg class="abs brand-tab" width="272" height="77" viewBox="0 0 272 77"><path d="M0 0H215L272 77H0Z" fill="#fff"/></svg>
<div class="abs brand"><i></i>VEXLAND<br>REBUILDERS</div>

<nav class="abs nav">
  <a class="active" style="left:318px">HOME</a>
  <a style="left:405px">ABOUT US</a>
  <a style="left:538px">SERVICE &amp; PRODUCTS</a>
  <a style="left:653px">TIPS</a>
  <a style="left:758px">SPECIALIZATIONS</a>
  <a style="left:866px">BLOG</a>
  <a style="left:953px">CONTACT</a>
</nav>

<!-- we do -->
<div class="abs dots-field" role="img" aria-label="Faded halftone dot pattern"></div>
<h2 class="abs h2 wedo-title">We <em>do</em></h2>
<p class="abs wedo-text">We Serving the Marine, Heavy Duty, Specialty, and Automotive industries.<br>We sell and rebuild starters and alternators for automobiles, heavy duty equipment, forklifts, gradalls, man movers, bobcats, loaders, large tractors and trucks, just about any engine, golf carts, generators, etc.</p>
<a class="abs btn"><span>Read more</span><b><svg width="14" height="8" viewBox="0 0 14 8"><path d="M0 4H12M9 1l3 3-3 3" stroke="#fff" stroke-width="1.5" fill="none"/></svg></b></a>
<div class="abs photo-big" role="img" aria-label="Photo of hands working on an engine with a ratchet, red tinted"></div>
<div class="abs photo-small" role="img" aria-label="Photo of a mechanic's hands on an engine part"></div>

<!-- services -->
<svg class="abs svc-band" width="1200" height="599" viewBox="0 0 1200 599" role="img" aria-label="Light grey textured band">
  <defs><linearGradient id="band" x1="0" x2="1" y1="0" y2="1"><stop offset="0" stop-color="#e4e4e4"/><stop offset="1" stop-color="#ececec"/></linearGradient></defs>
  <path d="M0 0H659L925 300L651 599H0Z" fill="url(#band)"/>
</svg>
<h2 class="abs h2 svc-title"><span><em>SERVICES</em> WE PROVIDE</span></h2>
<p class="abs svc-sub">YOUR SOURCE FOR NEW AND HIGH QUALITY REBUILT STARTERS &amp; ALTERNATORS</p>

<div class="abs svc-img" style="left:221px;background:linear-gradient(135deg,#ddd,#8a8a8a)" role="img" aria-label="Photo of a high amp alternator"></div>
<div class="abs svc-img" style="left:480px;background:linear-gradient(135deg,#c9803a,#6e7f8e)" role="img" aria-label="Photo of a magnifying glass on a keyboard"></div>
<div class="abs svc-img" style="left:737px;background:linear-gradient(135deg,#5a6f98,#d2a248)" role="img" aria-label="Photo of a worker with gloves and cables"></div>

<div class="abs svc-card light" style="left:239px">
  <div class="svc-icon"><svg width="26" height="22" viewBox="0 0 26 22"><rect x="2" y="2" width="22" height="14" rx="2" fill="none" stroke="#fff" stroke-width="2"/><path d="M7 7h12M7 11h12M9 20h8" stroke="#fff" stroke-width="2"/></svg></div>
  CUSTOM BUILT HIGH<br>AMP ALTERNATORS</div>
<div class="abs svc-card dark" style="left:497px">
  <div class="svc-icon"><svg width="24" height="24" viewBox="0 0 24 24"><circle cx="14" cy="10" r="6" fill="none" stroke="#222" stroke-width="2"/><path d="M9 15 3 21" stroke="#222" stroke-width="2.5"/></svg></div>
  HARD TO FIND<br>APPLICATIONS</div>
<div class="abs svc-card dark" style="left:754px">
  <div class="svc-icon"><svg width="24" height="26" viewBox="0 0 24 26"><path d="M6 2v8a6 6 0 0 0 12 0V2M12 16v8" fill="none" stroke="#222" stroke-width="2"/></svg></div>
  CUSTOM BUILT HIGH<br>AMP ALTERNATORS</div>

<!-- blog -->
<h2 class="abs h2 blog-title"><span>LATEST <em>BLOG</em></span></h2>
<p class="abs blog-sub">READ OUR LATEST BLOG POST</p>

<article class="abs post" style="left:221px">
  <div class="post-img" role="img" aria-label="Photo of a mechanic in blue sleeves working on an engine"></div>
  <div class="post-date">December 25, 2018 lorem, ipsum</div>
  <div class="post-meta"><span><i></i>By Smith</span><span><i></i>0 likes</span><span><i></i>0 comments</span></div>
  <h3>Lorem Ipsum</h3>
  <p>Lorem Ipsum is simply dummy text of the more printing and typesetting industry</p>
  <a class="more">VIEW DETAILS &nbsp;»</a>
</article>
<article class="abs post" style="left:501px">
  <div class="post-img" role="img" aria-label="Photo of a mechanic in blue sleeves working on an engine"></div>
  <div class="post-date">December 25, 2018 lorem, ipsum</div>
  <div class="post-meta"><span><i></i>By Smith</span><span><i></i>0 likes</span><span><i></i>0 comments</span></div>
  <h3>Lorem Ipsum</h3>
  <p>Lorem Ipsum is simply dummy text of the more printing and typesetting industry</p>
  <a class="more">VIEW DETAILS &nbsp;»</a>
</article>
<div class="abs side">
  <div class="side-item"><h4>Lorem Ipsum</h4><p>December 25, 2018 lorem, ipsum</p></div>
  <div class="side-item"><h4>Lorem Ipsum</h4><p>December 25, 2018 lorem, ipsum</p></div>
  <div class="side-item"><h4>Lorem Ipsum</h4><p>December 25, 2018 lorem, ipsum</p></div>
  <a class="more">READ MORE &nbsp;»</a>
</div>

<!-- contact band -->
<div class="abs contact"></div>
<div class="abs contact-col" style="left:180px">
  <svg width="26" height="26" viewBox="0 0 24 24"><path d="M6.6 10.8a15 15 0 0 0 6.6 6.6l2.2-2.2a1 1 0 0 1 1-.25 11 11 0 0 0 3.6.6 1 1 0 0 1 1 1V20a1 1 0 0 1-1 1A17 17 0 0 1 3 4a1 1 0 0 1 1-1h3.5a1 1 0 0 1 1 1 11 11 0 0 0 .6 3.6 1 1 0 0 1-.25 1Z" fill="#fff"/></svg>
  <h5>Have a question? call us now</h5>808 - 555 - 0142<br>808 - 555 - 0142<a>Contact Us</a></div>
<div class="abs divider" style="left:472px"></div>
<div class="abs contact-col" style="left:488px">
  <svg width="36" height="26" viewBox="0 0 36 26"><rect width="36" height="26" fill="#fff"/><path d="M1 1l17 13L35 1" stroke="#16234a" stroke-width="2.5" fill="none"/></svg>
  <h5>Need support? Drop us an email</h5>hello@vexlandrib.com<br>hello@vexlandrib.com<a>Fill Our Form</a></div>
<div class="abs divider" style="left:800px"></div>
<div class="abs contact-col" style="left:772px">
  <svg width="28" height="28" viewBox="0 0 28 28"><circle cx="14" cy="14" r="13" fill="#fff"/><path d="M14 7v8h6" stroke="#16234a" stroke-width="2.5" fill="none"/></svg>
  <h5>We are open on</h5>Mon – Fri 08:00 – 6:00,<br>Sat09:00 – 2:00<a>View More</a></div>

<div class="abs map" role="img" aria-label="Street map showing the shop location"></div>

<!-- footer -->
<footer class="abs footer"></footer>
<div class="abs foot-brand"><i></i>VEXLAND<br>REBUILDERS</div>
<p class="abs foot-about">Ipsum has been the industry's standard dummy text ever since the 1500s,when an unknown printer took a galley of type and scrambled it to make a type specimen book.</p>
<div class="abs foot-col" style="left:492px"><h6>USEFULL LINKS</h6>
  <ul><li>HOME</li><li>ABOUT US</li><li>SERVICE &amp; PRODUCTS</li><li>TIPS</li><li>SPECIALIZATIONS</li><li>BLOG</li><li>CONTACT</li></ul></div>
<div class="abs foot-col" style="left:667px"><h6>MARKET SECTORS</h6>
  <ul><li>Lorem Ipsum</li><li>Lorem Ipsum</li><li>Lorem Ipsum</li><li>Lorem Ipsum</li><li>Lorem Ipsum</li></ul></div>
<div class="abs foot-col" style="left:853px"><h6>NEWSLETTER</h6>
  <p class="news-text">You can be always up to date with our company news!</p>
  <div class="news-form"><span>email@domain.com</span><b>OK</b></div>
  <div class="follow">FOLLOW US ON: <i></i><i></i></div></div>
<div class="abs foot-line"></div>
<p class="abs copy">COPYRIGHT © 2019, Vexland Rebuilders, INC. ALL RIGHTS RESERVED</p>

</body>
</html>
```